Direct Response Landing Page for Paid Search Campaigns for KinTracer.net

KinTracer.net is a leading people search / public records company, providing consumers with instant, accurate access to public records. We are a direct response org focused on engaging the user and converting the user to a customer. Our product returns instant search results based on a name or phone search. We are looking for a landing page to test out, against our current "Home Page." We will drive traffic to this page via paid search terms (ie., "people search, find people"). We would like a landing page with a headline, search forms, CTA Search button, with features/beneifts about the service and company. Specific Key Messaging will be provided.

Target Market(s)

Consumers. Skew slightly female, ages 40+

Industry/Entity Type

It Company

Number of Pages Required

1 page

Font styles to use
Sans Serif

Requirements
Must have
• Use of Logo; upper left corner, consistent w/ KinTracer.net.
• Use of two HTML search forms (prefer a toggle between the two). Users must type in a search query in a search form for either:
• 1. First Name, Last Name, City, State
• 2. Phone # (area code w/ phone #)
• Call to Action: "Search" button
Should not have
• Should not include KinTracer.net's standard nav at the top.

```html
<!DOCTYPE html>
<html lang="en">
<head>
<meta charset="utf-8">
<title>KinTracer.net – Find Anyone</title>
<link rel="stylesheet" href="https://fonts.googleapis.com/css2?family=Questrial&family=Nunito:wght@700;800&family=Arimo:wght@400;700&display=swap">
<style>
  :root {
    --brand-blue: #3a8fd0;
    --panel-blue: #3b8bcb;
    --footer-blue: #2d86c8;
    --navy: #003f6e;
    --tab-grey: #555759;
    --heading-grey: #4a4a4a;
    --text-dark: #333333;
    --cta-green: #1a8f3f;
    --white: #ffffff;
    --input-text: #2f7fc0;
  }
  * { box-sizing: border-box; margin: 0; padding: 0; }
  html, body { width: 1198px; height: 1200px; overflow: hidden; background: var(--white); }
  body { position: relative; font-family: "Arimo", Arial, sans-serif; color: var(--text-dark); }

  .site-header { position: absolute; top: 0; left: 0; width: 1198px; height: 100px; background: var(--white); }
  .brand { position: absolute; display: flex; align-items: center; gap: 10px; font-family: "Questrial", sans-serif; font-size: 36px; }
  .brand-dot { width: 40px; height: 40px; border-radius: 50%; background: var(--brand-blue); }
  .site-header .brand { left: 100px; top: 26px; color: var(--brand-blue); }
  .tagline { position: absolute; left: 487px; top: 50px; font-family: "Questrial", sans-serif; font-size: 26px; color: var(--brand-blue); letter-spacing: 0.2px; }

  .hero { position: absolute; top: 100px; left: 0; width: 1198px; height: 492px; }
  .hero-photo { position: absolute; inset: 0;
    background: linear-gradient(90deg, #d9e6ef 0%, #eef3f7 25%, #dfe9f1 55%, #c9d9e6 80%, #bfd1e0 100%); }
  .hero-photo::after { content: ""; position: absolute; left: 0; right: 0; bottom: 0; height: 70px;
    background: linear-gradient(180deg, rgba(120,110,150,0) 0%, rgba(110,95,140,0.45) 100%); }

  .search-tabs { position: absolute; left: 569px; top: 54px; display: flex; }
  .search-tab { height: 41px; display: flex; align-items: center; justify-content: center; font-family: "Questrial", sans-serif; font-size: 19px; color: var(--white); }
  .search-tab.is-active { width: 211px; background: var(--panel-blue); }
  .search-tab.is-idle { width: 207px; background: var(--tab-grey); }

  .search-form { position: absolute; left: 569px; top: 95px; width: 531px; height: 187px; background: var(--panel-blue); padding: 29px 14px 0 16px; }
  .field-row { display: flex; gap: 9px; margin-bottom: 8px; }
  .field { width: 246px; height: 36px; background: var(--white); padding-left: 13px; display: flex; align-items: center; font-size: 14px; color: var(--input-text); }
  .search-button { margin-top: 14px; width: 501px; height: 46px; background: var(--navy); color: var(--white); display: flex; align-items: center; justify-content: center; font-family: "Arimo", sans-serif; font-weight: 700; font-size: 17px; letter-spacing: 0.3px; }

  .about-box { position: absolute; left: 569px; top: 282px; width: 531px; height: 146px; background: rgba(255,255,255,0.88); padding: 20px 30px; }
  .about-box h2 { font-family: "Questrial", sans-serif; font-weight: 700; font-size: 23px; color: var(--heading-grey); margin-bottom: 12px; -webkit-text-stroke: 0.6px var(--heading-grey); }
  .about-box ul { list-style: none; font-family: "Questrial", sans-serif; font-size: 14px; color: var(--heading-grey); letter-spacing: 0.3px; }
  .about-box li { position: relative; padding-left: 16px; line-height: 19.5px; }
  .about-box li::before { content: "•"; position: absolute; left: -3px; font-size: 10px; }

  .feature { position: absolute; top: 660px; width: 300px; text-align: center; }
  .feature-icon { height: 84px; display: flex; align-items: flex-end; justify-content: center; }
  .feature h3 { font-family: "Nunito", sans-serif; font-weight: 800; font-size: 25px; color: var(--brand-blue); margin-top: 16px; }
  .feature p { font-size: 14.5px; line-height: 17px; color: var(--text-dark); margin-top: 6px; }
  .learn-more { position: absolute; top: 214px; left: 75px; width: 153px; height: 36px; background: var(--cta-green); color: var(--white);
    font-family: "Nunito", sans-serif; font-weight: 800; font-size: 13px; display: flex; align-items: center; padding-left: 37px; }
  .learn-more::before { content: ""; position: absolute; left: 10px; top: 14px; border-left: 5px solid var(--white); border-top: 4px solid transparent; border-bottom: 4px solid transparent; }

  .site-footer { position: absolute; top: 1028px; left: 0; width: 1198px; height: 172px; background: var(--footer-blue); color: var(--white); }
  .site-footer .brand { left: 102px; top: 48px; color: var(--white); }
  .site-footer .brand-dot { background: var(--white); }
  .footer-heading { position: absolute; font-family: "Questrial", sans-serif; font-size: 19px; }
  .follow { left: 524px; top: 38px; }
  .social-list { position: absolute; left: 524px; top: 82px; display: flex; gap: 9px; }
  .social-square { width: 29px; height: 29px; background: rgba(255,255,255,0.85); }
  .newsletter { left: 783px; top: 41px; }
  .newsletter-note { position: absolute; left: 781px; top: 66px; font-size: 11px; color: #e4f0fa; }
  .email-field { position: absolute; left: 780px; top: 87px; width: 233px; height: 27px; background: #d6e6f3; color: #2f7fc0; font-size: 11px; padding-left: 9px; display: flex; align-items: center; }
  .subscribe { position: absolute; left: 1017px; top: 87px; width: 83px; height: 27px; background: var(--navy); font-size: 11px; display: flex; align-items: center; justify-content: center; }
</style>
</head>
<body>
  <header class="site-header">
    <div class="brand"><span class="brand-dot"></span>KinTracer.net</div>
    <div class="tagline">Since 1999, Your Trusted Online People Search Source</div>
  </header>

  <section class="hero">
    <div class="hero-photo" role="img" aria-label="Photo of a smiling woman in a teal top using a tablet at a bright café table with a drink"></div>

    <div class="search-tabs">
      <div class="search-tab is-active">Search By Name</div>
      <div class="search-tab is-idle">Search By Phone</div>
    </div>
    <form class="search-form">
      <div class="field-row"><div class="field">First Name</div><div class="field">Last Name</div></div>
      <div class="field-row"><div class="field">City</div><div class="field">State</div></div>
      <div class="search-button">SEARCH</div>
    </form>
    <div class="about-box">
      <h2>WHO WE ARE</h2>
      <ul>
        <li>Launched online in 1999</li>
        <li>Leading Data-as-a-Service Public Records Organization</li>
        <li>Privacy and Security are paramount to our Organization</li>
      </ul>
    </div>
  </section>

  <section class="feature" style="left:103px;">
    <div class="feature-icon">
      <svg width="52" height="70" viewBox="0 0 52 70" fill="var(--brand-blue)">
        <circle cx="26" cy="20" r="17" fill="none" stroke="var(--brand-blue)" stroke-width="4"/>
        <path d="M26 10v10l7 5" fill="none" stroke="var(--brand-blue)" stroke-width="3"/>
        <path d="M2 70V56c0-9 8-14 16-14h16c8 0 16 5 16 14v14z"/>
        <path d="M23 42h6l-1 6 3 14-5 6-5-6 3-14z" fill="#fff"/>
      </svg>
    </div>
    <h3>Save Time</h3>
    <p>KinTracer.net has people, phone,<br>background, property and criminal, at your fingertips.</p>
    <div class="learn-more">LEARN MORE</div>
  </section>

  <section class="feature" style="left:455px; top:662px;">
    <div class="feature-icon">
      <svg width="70" height="72" viewBox="0 0 70 72" fill="var(--brand-blue)">
        <path d="M36 2h34v30H48l-8 8 2-8h-6z"/>
        <text x="53" y="26" font-family="Arimo, sans-serif" font-weight="700" font-size="24" fill="#fff" text-anchor="middle">$</text>
        <circle cx="17" cy="34" r="11"/>
        <path d="M0 72V58c0-8 6-12 13-12h10c7 0 13 4 13 12v14z"/>
        <path d="M16 46h4l2 16-4 5-4-5z" fill="#fff"/>
      </svg>
    </div>
    <h3>Save $</h3>
    <p>We do the vetting for you to access local,<br>state and nationwide records =&nbsp; delivering<br>you AFFORDABLE UNLIMITED access.</p>
    <div class="learn-more">LEARN MORE</div>
  </section>

  <section class="feature" style="left:801px;">
    <div class="feature-icon">
      <svg width="74" height="50" viewBox="0 0 74 50" fill="var(--brand-blue)">
        <circle cx="6" cy="14" r="4"/><rect x="1" y="19" width="10" height="16" rx="2"/><rect x="3" y="34" width="6" height="12"/>
        <circle cx="68" cy="14" r="4"/><rect x="63" y="19" width="10" height="16" rx="2"/><rect x="65" y="34" width="6" height="12"/>
        <circle cx="19" cy="10" r="5"/><rect x="13" y="16" width="12" height="18" rx="2"/><rect x="15" y="33" width="8" height="14"/>
        <circle cx="55" cy="10" r="5"/><rect x="49" y="16" width="12" height="18" rx="2"/><rect x="51" y="33" width="8" height="14"/>
        <circle cx="37" cy="6" r="6"/><rect x="29" y="13" width="16" height="22" rx="2"/><rect x="32" y="34" width="10" height="16"/>
      </svg>
    </div>
    <h3>Comprehensive</h3>
    <p>We Provide Instant Access to Billions of<br>People Search &amp; Background Records</p>
    <div class="learn-more">LEARN MORE</div>
  </section>

  <footer class="site-footer">
    <div class="brand"><span class="brand-dot"></span>KinTracer.net</div>
    <div class="footer-heading follow">Follow Us</div>
    <div class="social-list">
      <span class="social-square" role="img" aria-label="Social network link"></span>
      <span class="social-square" role="img" aria-label="Social network link"></span>
      <span class="social-square" role="img" aria-label="Social network link"></span>
    </div>
    <div class="footer-heading newsletter">Newsletter</div>
    <div class="newsletter-note">Subscribe to recieve inspiration, ideas, and news in your inbox.</div>
    <div class="email-field">Email Address</div>
    <div class="subscribe">Subscribe</div>
  </footer>
</body>
</html>
```